Core values in our company OPK (Residency and Relocation)

Do good:
1. Being Direct and communicative for the benefit of all parties
2. Working for the Benefit of the company, client and team members
3. Wanting to improve to create a better impact
4. Having healthy rivalry
Be ahead of curve:
1. Having the confidence to break through barriers which arise
2. Desire to grow and learn towards establishment and agreed goal
3. Getting off the sidelines and get into the game
4. Keeping the end game in mind having due regard to processes and milestones
5. Self starter and works on own initiative
6. Diligent and impactful in your field of responsibility
Truth and Honesty
2. Have the confidence and ability to speak what you really want to communicate
3. Being truthful to yourself, clients and colleagues to find the innovations that lie within
4. Seeking the truth by opening things up for discussion
5. Being Optimistic
Background Information on our Company:OPK is a professional law firm in London Docklands. We caters for both private and corporate clients ranging from highly regarded and established law firms to boutique and niche immigration practices. We also specialises in expert legal advice and prides itself on providing services that go beyond the expectations of its clients.
What we need: We need a Poster about Truth and Honesty, this is to show one of our values as a company. It will need to be vibrant and straight to the point. Colours can be orange grey white and yellow. Attached is our company logo.
Reason: To remind colleagues that this is one of our main values and it is instilled in our company.
Things we would like:
1. To create a point of focus
2. Use shapes to create visual interest
3. Use creative illustrations
4. Take the viewer’s focus on a journey with clever perspective
Industry/Entity Type
Legal
Requirements
Must have
- a globe (Picture)
- Do good:
- 1. Being Direct and communicative for the benefit of all parties
- 2. Working for the Benefit of the company, client and team members
- 3. Wanting to improve to create a better impact
- 4. Having healthy rivalry
- Be ahead of curve:
- 1. Having the confidence to break through barriers which arise
- 2. Desire to grow and learn towards establishment and agreed goal
- 3. Getting off the sidelines and get into the game
- 4. Keeping the end game in mind having due regard to processes and milestones
- 5. Self starter and works on own initiative
- 6. Diligent and impactful in your field of responsibility
- Truth and Honesty
- 2. Have the confidence and ability to speak what you really want to communicate
- 3. Being truthful to yourself, clients and colleagues to find the innovations that lie within
- 4. Seeking the truth by opening things up for discussion
- 5. Being Optimistic

```html
<!DOCTYPE html>
<html lang="en">
<head>
<meta charset="utf-8">
<title>OPK Core Values Poster</title>
<link href="https://fonts.googleapis.com/css2?family=Noto+Serif:wght@700&family=Mulish:wght@700;800&display=swap" rel="stylesheet">
<style>
  :root{
    --stage:#3a3a3c;
    --paper:#ffffff;
    --mist:#efefef;
    --panel:#e6e6e6;
    --ink:#2f2f2f;
    --ink-soft:#4a4a4a;
    --orange:#f39200;
    --orange-deep:#ee7d00;
    --yellow:#ffc21a;
    --chart:#c8102e;
    --globe:#2d9ad8;
    --globe-light:#7cc6ee;
    --footer:#3b3b3b;
    --cloud:#dcdcdc;
  }
  *{box-sizing:border-box;margin:0;padding:0}
  html,body{width:1200px;height:2163px;overflow:hidden;background:var(--stage)}
  .poster{position:absolute;left:40px;top:295px;width:1120px;height:1574px;background:var(--mist);overflow:hidden;font-family:"Mulish",sans-serif}
  .layer{position:absolute;left:0;top:0}
  .brand{position:absolute;left:80px;top:40px;display:flex;flex-direction:column;align-items:flex-start}
  .brand-name{font-family:"Noto Serif",serif;font-weight:700;font-size:92px;line-height:1;color:var(--orange);display:flex;align-items:center;gap:16px}
  .brand-dot{width:22px;height:22px;border-radius:50%;background:var(--orange)}
  .brand-tag{font-family:"Noto Serif",serif;font-weight:700;font-size:21px;color:var(--ink);margin-top:10px;letter-spacing:.3px}
  .title{position:absolute;left:40px;top:770px;font-family:"Noto Serif",serif;font-weight:700;font-size:47px;line-height:1.05;color:var(--ink)}
  .pill{position:absolute;height:64px;display:flex;align-items:center;padding-left:38px;font-family:"Noto Serif",serif;font-weight:700;font-size:27px;color:var(--ink);background:linear-gradient(90deg,var(--orange-deep),var(--orange) 45%,var(--yellow));border-radius:0 34px 34px 0}
  .pill-truth{left:0;top:927px;width:355px}
  .pill-good{left:489px;top:699px;width:357px;border-radius:16px 34px 34px 16px}
  .pill-ahead{left:507px;top:1001px;width:347px;border-radius:16px 34px 34px 16px}
  .values{position:absolute;list-style:none}
  .values li{position:absolute;left:0;display:flex;gap:12px;font-weight:800;font-size:17.5px;line-height:1.2;color:var(--ink-soft)}
  .values li svg{flex:none;width:20px;height:20px;margin-top:1px}
  .values-truth{left:44px;top:0;width:390px}
  .values-truth li{text-align:justify;width:380px}
  .values-good,.values-ahead{left:516px;top:0;width:580px}
  .values-good li,.values-ahead li{width:570px}
  .footer-site{position:absolute;left:570px;top:1463px;display:flex;align-items:center;gap:12px;font-family:"Noto Serif",serif;font-weight:700;font-size:29px;color:#f4f4f4}
  .footer-social{position:absolute;left:570px;top:1520px;display:flex;gap:12px}
  .footer-social span{width:32px;height:32px;border-radius:50%;border:2.5px solid var(--orange)}
</style>
</head>
<body>
<main class="poster">
  <svg class="layer" width="1120" height="1574" viewBox="0 0 1120 1574" aria-hidden="true">
    <defs>
      <radialGradient id="globeTone" cx="40%" cy="40%" r="70%">
        <stop offset="0" stop-color="var(--globe-light)"/>
        <stop offset="1" stop-color="var(--globe)"/>
      </radialGradient>
    </defs>
    <!-- header background -->
    <rect x="0" y="0" width="1120" height="680" fill="var(--mist)"/>
    <!-- cloud pills -->
    <g fill="var(--cloud)">
      <rect x="600" y="70" width="120" height="24" rx="12"/>
      <rect x="960" y="150" width="110" height="22" rx="11"/>
      <rect x="330" y="300" width="95" height="20" rx="10"/>
      <rect x="60" y="380" width="120" height="22" rx="11"/>
      <rect x="1000" y="560" width="90" height="20" rx="10"/>
      <rect x="860" y="330" width="70" height="18" rx="9"/>
    </g>
    <!-- trend line -->
    <polyline points="0,448 216,310 310,376 489,336 600,420 953,466 1120,427" fill="none" stroke="var(--chart)" stroke-width="4"/>
    <g fill="var(--chart)">
      <circle cx="216" cy="310" r="8"/><circle cx="310" cy="376" r="8"/><circle cx="489" cy="336" r="8"/><circle cx="953" cy="466" r="8"/>
    </g>
    <!-- illustration area -->
    <circle cx="716" cy="414" r="250" fill="none" stroke="#1f2f55" stroke-width="3" stroke-dasharray="9 9"/>
    <circle cx="716" cy="414" r="227" fill="url(#globeTone)" role="img" aria-label="Illustration: a businessman in a suit with a magnifying glass and briefcase standing over a blue world globe"/>
    <!-- logo tab -->
    <path d="M0 0 H480 C430 0 440 214 370 214 H0 Z" fill="var(--paper)"/>
    <path d="M480 4 C430 4 440 214 370 214 H0" fill="none" stroke="var(--orange)" stroke-width="5"/>
    <rect x="470" y="0" width="650" height="8" fill="var(--orange)"/>
    <!-- lower panels -->
    <rect x="0" y="675" width="480" height="899" fill="var(--panel)"/>
    <path d="M470 675 H1120 V1442 H470 C500 1340 500 760 470 675 Z" fill="var(--paper)"/>
    <path d="M470 675 C500 760 500 1340 470 1442 C420 1500 390 1560 360 1574" fill="none" stroke="var(--paper)" stroke-width="14"/>
    <rect x="455" y="1442" width="665" height="132" fill="var(--footer)"/>
    <rect x="455" y="1440" width="665" height="5" fill="var(--orange)"/>
  </svg>

  <div class="brand">
    <div class="brand-name"><span class="brand-dot"></span>OPK</div>
    <div class="brand-tag">residency and relocation</div>
  </div>

  <h1 class="title">THE CORE<br>VALUES OF OPK</h1>

  <div class="pill pill-truth">Truth and Honesty:</div>
  <div class="pill pill-good">Do good:</div>
  <div class="pill pill-ahead">Be ahead of curve:</div>

  <svg width="0" height="0" style="position:absolute">
    <symbol id="tick" viewBox="0 0 20 20"><circle cx="10" cy="10" r="8" fill="none" stroke="#f39200" stroke-width="2"/><path d="M6 10.5 L9 13 L14.5 7" fill="none" stroke="#f39200" stroke-width="2.2"/></symbol>
  </svg>

  <ul class="values values-truth">
    <li style="top:1047px"><svg><use href="#tick"/></svg>Having the confidence to break through barriers which arise</li>
    <li style="top:1132px"><svg><use href="#tick"/></svg>Have the confidence and ability to speak what you really want to communicate</li>
    <li style="top:1233px"><svg><use href="#tick"/></svg>Being truthful to yourself, clients and colleagues to find the innovations that lie within</li>
    <li style="top:1335px"><svg><use href="#tick"/></svg>Seeking the truth by opening things up for discussion</li>
    <li style="top:1415px"><svg><use href="#tick"/></svg>Being Optimistic</li>
  </ul>

  <ul class="values values-good">
    <li style="top:806px"><svg><use href="#tick"/></svg>Being Direct and communicative for the<br>benefit of all parties</li>
    <li style="top:865px"><svg><use href="#tick"/></svg>Working for the Benefit of the company, client<br>and team members</li>
    <li style="top:924px"><svg><use href="#tick"/></svg>Wanting to improve to create a better impact</li>
    <li style="top:966px"><svg><use href="#tick"/></svg>Having healthy rivalry</li>
  </ul>

  <ul class="values values-ahead">
    <li style="top:1108px"><svg><use href="#tick"/></svg>Having the confidence to break through<br>barriers which arise</li>
    <li style="top:1172px"><svg><use href="#tick"/></svg>Desire to grow and learn towards establishment<br>and agreed goal</li>
    <li style="top:1236px"><svg><use href="#tick"/></svg>Getting off the sidelines and get into the game</li>
    <li style="top:1282px"><svg><use href="#tick"/></svg>Keeping the end game in mind having due<br>regard to processes and milestones</li>
    <li style="top:1348px"><svg><use href="#tick"/></svg>Self starter and works on own initiative</li>
    <li style="top:1392px"><svg><use href="#tick"/></svg>Diligent and impactful in your field of responsibility</li>
  </ul>

  <div class="footer-site">
    <svg width="28" height="28" viewBox="0 0 28 28" aria-hidden="true"><g fill="none" stroke="#f39200" stroke-width="2"><circle cx="14" cy="14" r="12"/><ellipse cx="14" cy="14" rx="5" ry="12"/><path d="M2 14 H26 M4 8 H24 M4 20 H24"/></g></svg>
    Opkrelocation.com
  </div>
  <div class="footer-social" aria-hidden="true">
    <span></span><span></span><span></span><span></span><span></span><span></span><span></span><span></span>
  </div>
</main>
</body>
</html>
```